International Property Consultancy

Brief Overview:

I need a dynamic and well designed website that is easy to use and understand. It has to be unique and different to generic templates that most websites seem to be these days. PLEASE NO GENERIC TEMPLATES FROM THE INTERNET.

Our business has 10 years experience working on struggling international developments that we then work in-house for to turn around and brings bout success. We stay within a project often for long periods of time until success is achieved. We are unique in our approach and completely different to the standard routes to market for many developments. The site is for developers to see what we have done in regards to previous projects, as such we want to incorporate video into this site with a strong design aesthetic. There will be videos of the past projects we have worked on, which will act as case studies.

I like very simple but punchy websites, that people can navigate and understand very easily. Also a big fan of unique and well thought out design aesthetic.

Initial Site layout thoughts:

1) Homepage:
2) About Us
3) What we've done / Work
This part has the projects we have worked on (France, Portugal, London, Morocco). Each one will have some video content and photo images, but also would be good to have a succinct way to mention what we did and the successes in a clever and punchy way.

4) Contact Us

* This is just a guideline. Would be open to input and creative direction on your own part.

*More details and websites we like can be seen in the brief doc attached.

PLEASE VIEW THE WIREFRAME WORD DOC ATTACHED.

Here there are also some more examples to help:

Here are just a few examples of websites and what I like about them:

- www.velmoro.com (clean, nice geometric design aesthetic, good animation when loading and changing pages well thought out all though also coulee be considered a bit dull and basic after the initial homepage slide)
- https://www.farbridgehub.net (Clean site, quite clinical, lacks video content and doesn't engage greatly).
- https://ruskotile.com (minimal, and like how it mixes the design aesthetic more with video and photo content)

- https://www.amberquillworks.com (like the layout of this and how it displays the projects and work section)

- https://brisk.com (Good use of video content)

- https://loomfield.studio (minimal to the point and mixes design with video and animation etc...)

Here is another couple of cool websites that may help give you some direction: https://halvenquay.com www.brisk.com

Hi there, One of the things I thought would be good on the homepage is to add the logo with a 'digital landscape' before flicking down into a slide with video content of the projects... Just an idea but have posted some pics in the brief. We would get this animated for the site. But if you have better ideas, please do run with them. Thanks,

Target Market(s)

Property developers

Number of Pages Required

4 page

Font styles to use
Other font styles liked:
• Read brief

Requirements
Must have
• Needs to be clean, dynamic and easy to follow on desktop and mobile. We will use it as a kind of portfolio website so will need to embed video of past projects we have worked on.

Read brief in docs.
Nice to have
• Clean
Should not have
• Not be another generic template website.
Not have random property stock photos. (We are not a property agency).

```html
<!DOCTYPE html>
<html lang="en">
<head>
<meta charset="utf-8">
<title>Norvalem — International Property Consultancy</title>
<link href="https://fonts.googleapis.com/css2?family=Montserrat:wght@400;500;600;700;800&display=swap" rel="stylesheet">
<style>
:root{
  --ink:#1f1f1f;
  --teal:#1e6f8c;
  --blue:#2490b5;
  --rail-dark:#27343d;
  --rail-hero:rgba(214,196,192,.82);
  --rail-soft:#f9ebe6;
  --footer:#f8e1da;
  --field:#e6e6e6;
  --white:#fff;
}
*{margin:0;padding:0;box-sizing:border-box}
html,body{width:1200px;height:2380px;overflow:hidden;background:var(--white)}
body{font-family:"Montserrat",sans-serif;color:var(--ink);position:relative}
.section{position:absolute;left:0;width:1200px}
.rail{position:absolute;left:150px;top:0;width:62px;height:100%}
.rail ul{list-style:none}
.rail li{position:absolute;left:50%;transform:translate(-50%,-50%) rotate(-90deg);white-space:nowrap;font-size:14px;font-weight:500;letter-spacing:.5px}
.rail .active{color:var(--blue);font-weight:600}
.rail--hero{background:var(--rail-hero)}
.rail--hero li{color:#8a8384}
.rail--dark{background:var(--rail-dark)}
.rail--dark li{color:var(--white)}
.rail--soft{background:var(--rail-soft)}
.rail--soft li{color:#4a4a4a}
.hero{top:0;height:583px}
.hero-bg{position:absolute;inset:0;background:linear-gradient(160deg,#121418 0%,#2c3e50 40%,#3e4c58 65%,#1b1d20 100%)}
.logo{position:absolute;left:226px;top:4px;font-size:36px;font-weight:500;color:var(--white);letter-spacing:.5px}
.search{position:absolute;left:1033px;top:22px}
.hero-title{position:absolute;left:230px;width:822px;top:196px;text-align:center;color:var(--white);font-size:24px;font-weight:800;line-height:36px}
.play{position:absolute;left:566px;top:347px;width:100px;text-align:center;color:var(--white);font-size:13px;font-weight:500}
.play svg{display:block;margin:0 auto 6px}
.about{top:583px;height:585px}
.about h2{position:absolute;left:226px;top:212px;width:560px;font-size:19px;line-height:21px;font-weight:700;color:var(--teal)}
.about p{position:absolute;left:226px;top:281px;width:830px;font-size:13.6px;line-height:22.4px}
.projects{top:1168px;height:583px}
.video{position:absolute;left:226px;top:14px;width:838px;height:359px;background:linear-gradient(180deg,#14202d 0%,#27394c 55%,#141a22 100%)}
.video svg{position:absolute;left:360px;top:166px}
.underlined{font-weight:700;display:inline-block;padding-bottom:3px;border-bottom:3px solid var(--teal)}
.project-title{position:absolute;left:226px;top:393px;font-size:19px;color:var(--blue);border-color:var(--blue)}
.project-text{position:absolute;left:226px;top:438px;width:840px;font-size:13.6px;line-height:22.6px}
.pager{position:absolute;left:226px;top:553px;width:824px;font-size:13px;color:var(--teal);font-weight:500}
.pager .prev{position:absolute;left:0;top:0}
.pager .count{position:absolute;left:366px;top:1px;color:var(--ink);font-size:11px}
.pager .next{position:absolute;right:0;top:-2px}
.contact{top:1751px;height:585px}
.contact h2{position:absolute;top:198px;font-size:19px;color:var(--teal)}
.contact .c-head{left:226px}
.contact .f-head{left:834px}
.field{position:absolute;height:30px;background:var(--field);font-size:10px;color:#555;padding:12px 8px 0;letter-spacing:.3px}
.send{position:absolute;left:226px;top:458px;width:130px;height:30px;background:var(--blue);color:var(--white);font-size:14px;font-weight:700;text-align:center;line-height:30px}
.social{position:absolute;left:836px;top:286px;list-style:none}
.social li{display:flex;align-items:center;height:20px;margin-bottom:19.7px;font-size:13px}
.social .dot{width:18px;height:18px;border-radius:50%;background:#262626;margin-right:12px}
.footer{top:2336px;height:44px;background:var(--footer);text-align:center;font-size:11px;color:#555;line-height:44px}
</style>
</head>
<body>

<section class="section hero">
  <div class="hero-bg" role="img" aria-label="Upward view of glass skyscrapers against a dusk sky"></div>
  <nav class="rail rail--hero"><ul>
    <li class="active" style="top:138px">HOME</li>
    <li style="top:233px">ABOUT US</li>
    <li style="top:342px">PROJECTS</li>
    <li style="top:461px">CONTACT US</li>
  </ul></nav>
  <div class="logo">norvalem.</div>
  <svg class="search" width="18" height="18" viewBox="0 0 18 18" fill="none" stroke="#fff" stroke-width="1.4"><circle cx="7.5" cy="7.5" r="5.5"/><line x1="11.5" y1="11.5" x2="16" y2="16"/></svg>
  <h1 class="hero-title">Consultancy Company That Helps International Property Developments Fulfil Their Potential.</h1>
  <div class="play">
    <svg width="26" height="26" viewBox="0 0 26 26" fill="none" stroke="#fff" stroke-width="1.3"><circle cx="13" cy="13" r="12"/><path d="M10.5 8.5l7 4.5-7 4.5z"/></svg>
    Play Vedio
  </div>
</section>

<section class="section about">
  <nav class="rail rail--dark"><ul>
    <li style="top:118px">HOME</li>
    <li class="active" style="top:214px">ABOUT US</li>
    <li style="top:324px">PROJECTS</li>
    <li style="top:443px">CONTACT US</li>
  </ul></nav>
  <h2>We specialise in the fulfilment of international property developments.</h2>
  <p>Norvalem is a consultancy company that helps international property developments fulfil their potential. The company has had great success over the last 10 years of turning around struggling property developments (often resort and investment) and making them reach their maximum potential.<br>We have completed projects in Portugal, London, France, Morocco, Brazil...</p>
</section>

<section class="section projects">
  <nav class="rail rail--soft"><ul>
    <li style="top:118px">HOME</li>
    <li style="top:214px">ABOUT US</li>
    <li class="active" style="top:324px">PROJECTS</li>
    <li style="top:443px">CONTACT US</li>
  </ul></nav>
  <div class="video" role="img" aria-label="Project video still: city skyline at night">
    <svg width="26" height="26" viewBox="0 0 26 26" fill="none" stroke="#fff" stroke-width="1.3"><circle cx="13" cy="13" r="12"/><path d="M10.5 8.5l7 4.5-7 4.5z"/></svg>
  </div>
  <h3 class="underlined project-title">France</h3>
  <p class="project-text">Lorem ipsum dolor sit amet, consectetur adipisicing elit, sed do eiusmod tempor incididunt ut labore et dolore magna aliqua. Ut enim ad minim veniam, quis nostrud exercitation ullamco laboris nisi ut aliquip ex ea commodo consequat. Duis aute irure dolor in reprehenderit in voluptate velit esse cillum dolore eu fugiat nulla pariatur.</p>
  <div class="pager">
    <span class="prev">‹&nbsp; Prev Project</span>
    <span class="count">1/4</span>
    <span class="next">Next Project &nbsp;›</span>
  </div>
</section>

<section class="section contact">
  <nav class="rail rail--dark"><ul>
    <li style="top:118px">HOME</li>
    <li style="top:214px">ABOUT US</li>
    <li style="top:324px">PROJECTS</li>
    <li class="active" style="top:443px">CONTACT US</li>
  </ul></nav>
  <h2 class="underlined c-head">Contacts</h2>
  <h2 class="underlined f-head">Fallow Us</h2>
  <div class="field" style="left:226px;top:278px;width:260px">Your Name*</div>
  <div class="field" style="left:500px;top:278px;width:260px">Last Name*</div>
  <div class="field" style="left:226px;top:323px;width:260px">Company Name*</div>
  <div class="field" style="left:500px;top:323px;width:260px">E-mail*</div>
  <div class="field" style="left:226px;top:368px;width:534px;height:74px;padding-top:9px">Message</div>
  <div class="send">Send</div>
  <ul class="social">
    <li><span class="dot"></span>www.friendsphere.com/Norvalem</li>
    <li><span class="dot"></span>www.chirpline.com/Norvalem</li>
    <li><span class="dot"></span>www.worknetic.com/Norvalem</li>
    <li><span class="dot"></span>www.pinboardly.com/Norvalem</li>
  </ul>
</section>

<footer class="section footer">Copyright © 2020 Norvalem</footer>

</body>
</html>
```